Photography Studio Prep Guide Design Needed

I have a prep guide I send to all parents who book a session - It is outdated and ugly. I want a gorgeous, clean, modern upscale look for the brochure I send.

I already have the text and can provide photos for the final design. I want the cover to be clean and upscale and modern, with a happy feel.

Target Market(s)

My clients for an upscale Newborn Photography Studio

Requirements
Must have
• space for my photos, an upscale clean feel
Nice to have
• I love color, but don't want the brochure to look busy. I love cream, white, pale pink.

```html
<!DOCTYPE html>
<html lang="en">
<head>
<meta charset="utf-8">
<title>Newborn Session Prep Guide</title>
<link href="https://fonts.googleapis.com/css2?family=Crete+Round&family=Poiret+One&family=Montserrat:wght@700&family=Playfair+Display:ital,wght@1,500&family=Bitter:ital,wght@1,800&family=Roboto+Condensed:wght@400;700&display=swap" rel="stylesheet">
<style>
:root{
  --bg:#2a2a2a;
  --paper:#ffffff;
  --wine:#6b2340;
  --ink:#2b2b2b;
  --body:#555555;
  --cream:#f1e6dc;
  --blush:#e9c3c6;
  --rule:#b98a9a;
  --spine:#ecdcc4;
}
*{margin:0;padding:0;box-sizing:border-box}
html,body{width:1200px;height:1048px;overflow:hidden;background:var(--bg)}
.canvas{position:relative;width:1200px;height:1048px}
.page{position:absolute;background:var(--paper);box-shadow:0 4px 14px rgba(0,0,0,.45)}
.cover{left:350px;top:94px;width:500px;height:386px}
.spread-left{left:75px;top:568px;width:499px;height:386px}
.spread-right{left:626px;top:568px;width:499px;height:386px}

.cover-panel{position:absolute;left:0;top:0;width:184px;height:386px;text-align:center}
.brand-mark{position:absolute;left:42px;top:86px;width:104px;height:104px;border:1.5px solid var(--wine);border-radius:50%;display:flex;align-items:center;justify-content:center;font-family:"Playfair Display",serif;font-style:italic;font-weight:500;color:var(--wine);font-size:11px;line-height:1.3;padding:10px}
.cover-title{position:absolute;left:0;width:184px;top:290px;font-family:"Crete Round",serif;font-size:34px;color:var(--wine);line-height:1}
.cover-sub{position:absolute;left:0;width:184px;top:332px;font-family:"Poiret One",sans-serif;font-size:13px;letter-spacing:1.5px;color:var(--ink)}
.cover-tag{position:absolute;left:0;width:184px;top:358px;font-family:"Montserrat",sans-serif;font-weight:700;font-size:8.5px;letter-spacing:1.6px;color:var(--ink)}
.cover-spine{position:absolute;left:184px;top:0;width:4px;height:386px;background:var(--spine)}
.cover-photo{position:absolute;left:188px;top:0;width:312px;height:386px;background:radial-gradient(circle at 50% 58%,#efc7cb 0,#f3d9d6 22%,var(--cream) 48%)}

.ph{position:absolute;background:linear-gradient(160deg,#e8d8c6,#c9b29b)}
.intro{position:absolute;left:0;width:499px;text-align:center}
.intro h1{margin-top:66px;font-family:"Playfair Display",serif;font-style:italic;font-weight:500;font-size:15px;color:var(--wine)}
.intro p{font-family:"Roboto Condensed",sans-serif;font-size:8px;line-height:10.3px;color:var(--ink);margin-top:3px}

.section{position:absolute}
.section h2{display:flex;align-items:center;gap:4px;font-family:"Bitter",serif;font-style:italic;font-weight:800;font-size:12px;color:var(--wine);border-bottom:.8px solid var(--rule);line-height:13px;padding-bottom:0}
.num{display:inline-block;width:13px;height:12px;background:var(--wine);color:#fff;font-style:normal;font-size:10px;text-align:center;line-height:12px}
.section .text{font-family:"Roboto Condensed",sans-serif;font-size:6.4px;line-height:9.9px;color:var(--body);text-align:justify;margin-top:2px}
.cols{display:flex;gap:14px;padding-left:16px}
.cols .text{flex:1}
.indent{padding-left:17px}
.text b{font-weight:700;color:var(--ink)}
.gap{height:9px}
</style>
</head>
<body>
<div class="canvas">

  <section class="page cover">
    <div class="cover-panel">
      <div class="brand-mark">Rosa Linden Photography</div>
      <div class="cover-title">NewBorn</div>
      <div class="cover-sub">SESSION</div>
      <div class="cover-tag">PREP GUIDE</div>
    </div>
    <div class="cover-spine"></div>
    <div class="cover-photo" role="img" aria-label="Sleeping newborn in a floral hanging basket with pink roses on a cream backdrop"></div>
  </section>

  <section class="page spread-left">
    <div class="intro">
      <h1>Parent Instructions &amp; Preparations</h1>
      <p>Congratulations on expecting a baby!<br>Here are my instructions to ensure a successful newborn photography session.<br>Please follow these instructions as closely as possible.</p>
    </div>

    <div class="section" style="left:26px;top:118px;width:448px">
      <h2><span class="num">1</span>NURSING</h2>
      <div class="cols">
        <p class="text">If you are nursing, please avoid eating anything spicy (hot sauce, hot peppers, curry, etc.) that might upset baby's tummy for 24 hours preceding your scheduled session.<br>Please if you are breastfeeding do NOT drink caffeine or coffee before your session – I know this is hard but baby will be wired if you have caffeine.</p>
        <p class="text">If you notice baby has a lot of gas after feedings please check with your pediatrician and bring gas drops (GentleTum or other brand) to your session. The most common reason a baby will not settle for a session is gas pressure/discomfort.</p>
      </div>
    </div>

    <div class="section" style="left:26px;top:200px;width:448px">
      <h2><span class="num">2</span>FEEDING</h2>
      <div class="cols">
        <p class="text">Feed the baby as much as possible in the 24 hours preceding your session – this will help minimize the amount baby needs to feed during the session, and will help baby sleep as long and as soundly as possible. Feed baby 2-3 hours before your session and not again until you arrive. This feeding is planned in your session time and it's not rushed.</p>
        <p class="text"><b>Please bring an extra bottle of formula or breastmilk to the session if possible – sometimes a small amount of milk in a bottle can quickly soothe a baby back to sleep without requiring a full feeding.</b> I will respect your wishes if you choose not to use a bottle, but please understand we may have to pass on some poses if baby will not settle in position, and I cannot use a bottle to soothe them into the pose.</p>
      </div>
    </div>

    <div class="ph" style="left:41px;top:290px;width:81px;height:80px;background:linear-gradient(160deg,#9fd3e0,#f1c84a)" role="img" aria-label="Newborn in aviator hat on a yellow toy plane"></div>
    <div class="ph" style="left:127px;top:290px;width:81px;height:80px;background:linear-gradient(160deg,#f3ece2,#c8834a)" role="img" aria-label="Newborn in knitted fox hat on cream fur"></div>
    <div class="ph" style="left:214px;top:290px;width:81px;height:80px;background:radial-gradient(circle,#2c3550 0,#3a4260 35%,#f2efe9 60%)" role="img" aria-label="Newborn wrapped in navy in a cream bowl"></div>
    <div class="ph" style="left:303px;top:290px;width:81px;height:80px;background:linear-gradient(160deg,#9fd3e0,#f1c84a)" role="img" aria-label="Newborn in aviator hat on a yellow toy plane"></div>
    <div class="ph" style="left:393px;top:290px;width:83px;height:80px;background:linear-gradient(160deg,#f3ece2,#c8834a)" role="img" aria-label="Newborn in knitted fox hat on cream fur"></div>
  </section>

  <section class="page spread-right">
    <div class="section" style="left:32px;top:39px;width:200px">
      <h2><span class="num">3</span>KEEP BABY AWAKE</h2>
      <div class="indent">
        <p class="text">Interact with, and keep baby awake for 2 hours preceding your appointment to make sure they are nice and sleepy for their session. A great way to do this is by giving baby a bath – which will get them nice and clean and keep them awake.</p>
        <div class="gap"></div>
        <p class="text">Also – keeping baby naked, in a diaper only is a good way to keep them awake and alert. This step is extremely important – otherwise it can take a long time to get baby to sleep, and we will have less time for photos.</p>
      </div>
    </div>

    <div class="section" style="left:32px;top:168px;width:200px">
      <h2><span class="num">4</span>CLOTHES</h2>
      <p class="text indent">Please dress baby in a simple loose sleeper we can just unsnap when you arrive – we want to keep baby as calm and happy as possible and want to avoid clothes we have to pull over their head. I provide all clothing/hats/props at your session.</p>
    </div>

    <div class="section" style="left:32px;top:246px;width:200px">
      <h2><span class="num">5</span>PACIFIER</h2>
      <p class="text indent">Please bring a pacifier – it can be very helpful during a session if a baby is fussy. Please note I only use the pacifier for a few minutes at a time to soothe into a pose. If you choose not to bring a pacifier I will respect your decision, but please understand we may have to pass on several poses if you do not bring one.</p>
    </div>

    <div class="section" style="left:264px;top:39px;width:198px">
      <h2><span class="num">6</span>STUDIO</h2>
      <div class="indent">
        <p class="text">My studio is kept VERY warm to make sure your baby is comfortable through the whole</p>
        <div class="gap" style="height:12px"></div>
        <p class="text">session. It will be around 75-80 degrees so please dress in layers for comfort. I will have cold bottles of water available during your session. Please note – if you ask me to turn the heat down, or tell me it is too warm for baby, I cannot guarantee any results for your session. Babies are used to 98.6 degrees in the womb, and a cold studio will wake baby immediately. Babies do not wear much during their sessions and lose heat quickly. If you ask me to turn the heat down, and baby is fussy I will finish the session with only swaddled poses, or with parents. It is not safe to put an awake, alert baby in any props.</p>
      </div>
    </div>

    <div class="section" style="left:264px;top:194px;width:198px">
      <h2><span class="num">6</span>YOURROLE</h2>
      <p class="text indent">Your role at this session is to sit back and relax. I need very little assistance during the session, and want you to take this time to rest, relax and enjoy the session. Feel free to nap, catch up on work, thank you notes, or whatever you like. If baby needs to feed during the session that will be your only task! I will occasionally ask for a spotter for safety on some poses.</p>
    </div>

    <div class="ph" style="left:330px;top:256px;width:169px;height:130px;background:radial-gradient(circle at 55% 55%,#f4e6dc 0,#efd8cc 28%,#8a7350 42%,#c6b56a 55%,#ffffff 72%)" role="img" aria-label="Newborn curled in a twig nest with blue and yellow wildflowers"></div>
  </section>

</div>
</body>
</html>
```